Career-focused learning application platform

We have a K-12 learning application platform designed for grades 6-12 that needs user interface improvements that provide a positive experience for all users (teachers and students). The learning platform provides career-focused math curriculum and career exploration resources. We would like to improve the user-interface with engaging design elements without taking away from the functionality and performance of the platform.

```html
<!DOCTYPE html>
<html lang="en">
<head>
<meta charset="utf-8">
<title>Trailpoint Careers – Sign in and Dashboard</title>
<link href="https://fonts.googleapis.com/css2?family=Poppins:wght@300;400;500;600;700&display=swap" rel="stylesheet">
<style>
:root{
  --frame:#428480;
  --orange:#E58A33;
  --teal:#22595A;
  --ink:#1E0B3E;
  --rust:#D95B35;
  --night:#2E2660;
  --violet:#5048A0;
  --paper:#F0F0F0;
  --white:#FFFFFF;
  --text:#222222;
  --heading:#3D3D3D;
  --line:#D6D6D6;
}
*{box-sizing:border-box;margin:0;padding:0}
html,body{width:1200px;height:2327px;overflow:hidden}
body{background:var(--frame);font-family:"Poppins",sans-serif;color:var(--text);position:relative}
.abs{position:absolute}
.panel{position:absolute;left:43px;width:1114px;background:var(--paper);overflow:hidden}
.topbar{position:absolute;left:0;top:0;width:100%;height:111px;background:var(--white)}
.brand{position:absolute;left:70px;top:40px;display:flex;align-items:center;gap:8px;font-weight:700;font-size:17px;color:var(--orange);letter-spacing:.2px}
.brand-dot{width:14px;height:14px;border-radius:50%;background:var(--orange)}
.pill{position:absolute;display:flex;align-items:center;justify-content:center;border-radius:30px;color:var(--white);font-weight:500}
.btn-signin-top{left:798px;top:34px;width:104px;height:44px;background:var(--orange);font-size:14px}
.btn-register-top{left:917px;top:34px;width:129px;height:44px;background:var(--teal);font-size:14px}
.nav{position:absolute;top:43px;font-size:14px;font-weight:600;color:var(--text);display:flex;align-items:center;gap:6px}
.nav svg{width:9px;height:6px}

/* sign in panel */
.signin-heading{left:70px;top:168px;font-size:41px;font-weight:700;line-height:46px;color:var(--heading)}
.sso{top:282px;width:196px;height:54px;background:var(--ink);font-size:19px;gap:14px}
.sso-mark{width:26px;height:26px;background:var(--white);border-radius:4px}
.sso-mark.round{border-radius:50%}
.divider-text{left:70px;top:372px;width:405px;display:flex;align-items:center;gap:10px;font-size:18px;font-weight:500;color:var(--ink)}
.divider-text span.rule{flex:1;height:1px;background:#9A9A9A}
.field{left:70px;width:474px;height:50px;border:1px solid var(--line);border-radius:25px;background:var(--white);font-size:13px;padding-left:24px;display:flex;align-items:center;color:var(--text)}
.btn-signin{left:70px;top:529px;width:151px;height:50px;background:var(--orange);font-size:14px}
.register-note{left:241px;top:542px;font-size:16px;font-weight:500;color:var(--ink)}
.register-note a{color:var(--rust);text-decoration:underline;text-underline-offset:4px}
.hero-art{position:absolute;left:571px;top:111px;width:543px;height:574px;background:linear-gradient(160deg,var(--night) 0%,var(--night) 38%,var(--violet) 62%,var(--violet) 100%)}

/* dashboard */
.section-title{left:74px;font-size:32px;font-weight:500;color:var(--text)}
.card{position:absolute;background:var(--white);border:1px solid var(--line);border-radius:12px}
.spot-title{left:24px;top:22px;font-size:24px;font-weight:700;color:var(--teal)}
.rule{position:absolute;height:1px;background:var(--line)}
.sub{font-size:20px;font-weight:500;color:var(--text)}
.body-copy{left:25px;top:128px;width:465px;font-size:14px;line-height:27.5px}
.earn-label{font-size:16px;font-weight:500}
.earn-value{font-size:16px;font-weight:700;color:var(--rust)}
.btn-learn{left:25px;top:356px;width:127px;height:48px;background:var(--teal);font-size:14px;font-weight:600}
.video{position:absolute;left:512px;top:87px;width:442px;height:318px;background:linear-gradient(110deg,#B9B9BB 0%,#8E8F93 45%,#5A5C64 75%,#2F4C8E 100%)}
.view-all{right:68px;top:718px;font-size:19px;font-weight:500;color:var(--orange);text-decoration:underline;text-underline-offset:4px}
.class-card{top:776px;width:304px;height:271px;overflow:hidden}
.class-head{position:absolute;left:0;top:0;width:100%;height:98px;padding:20px 0 0 22px;color:var(--white);font-size:16px;line-height:21px}
.class-head .who{display:flex;align-items:center;gap:12px;font-weight:500;font-size:17px}
.class-head .period{font-weight:600}
.class-head .course{font-weight:300;letter-spacing:.5px}
.class-brand{position:absolute;left:0;top:128px;width:100%;text-align:center;color:var(--orange);font-weight:700;font-size:17px}
.class-brand small{display:block;font-size:10px;color:var(--ink);letter-spacing:.5px;line-height:14px}
.btn-class{top:215px;left:82px;width:141px;height:38px;background:var(--orange);font-size:16px;font-weight:500}
.lessons-lead{left:24px;top:24px;font-size:20px;color:var(--teal)}
.col-head{font-size:20px;font-weight:500}
.cell{font-size:14.5px}
</style>
</head>
<body>

<!-- Sign in screen -->
<section class="panel" style="top:24px;height:685px">
  <header class="topbar">
    <div class="brand"><span class="brand-dot"></span>Trailpoint Careers</div>
    <span class="pill btn-signin-top">Sign in</span>
    <span class="pill btn-register-top">Register</span>
  </header>

  <h1 class="abs signin-heading">Sign in with your<br>school account</h1>
  <span class="pill sso" style="left:70px"><span class="sso-mark"></span>Northgate</span>
  <span class="pill sso" style="left:277px"><span class="sso-mark round"></span>Searchly</span>
  <div class="abs divider-text"><span class="rule"></span>Or Continue With<span class="rule"></span></div>
  <div class="abs field" style="top:408px">Email Address</div>
  <div class="abs field" style="top:468px">Password</div>
  <span class="pill btn-signin">Sign in</span>
  <p class="abs register-note">Need an account? <a>Register Here</a></p>

  <div class="hero-art" role="img" aria-label="Illustration of students among giant math tools, numbers, a compass, ruler and globe on a purple background"></div>
</section>

<!-- Dashboard screen -->
<section class="panel" style="top:739px;height:1543px">
  <header class="topbar">
    <div class="brand"><span class="brand-dot"></span>Trailpoint Careers</div>
    <span class="nav" style="left:364px">Home</span>
    <span class="nav" style="left:440px">Career Tools <svg viewBox="0 0 9 6"><path d="M0 0h9L4.5 6z" fill="#222"/></svg></span>
    <span class="nav" style="left:581px">Classes</span>
    <span class="nav" style="left:671px">Assessments</span>
    <span class="pill btn-signin-top">Sign in</span>
    <span class="pill btn-register-top">Register</span>
  </header>

  <h2 class="abs section-title" style="top:162px">Career Spotlights</h2>
  <article class="card" style="left:70px;top:228px;width:976px;height:450px">
    <h3 class="abs spot-title">Plumbers, Pipefitters, Steamfitters</h3>
    <div class="rule" style="left:24px;top:70px;width:928px"></div>
    <h4 class="abs sub" style="left:25px;top:86px">What they do</h4>
    <p class="abs body-copy">Lorem ipsum dolor sit amet, consectetur adipiscing elit, sed do eiusmod tempor incididunt ut labore et dolore magna aliqua. Ut enim ad minim veniam, quis nostrud exercitation ullamco sint occaecat cupidatat non proident, sunt in culpa.</p>
    <h4 class="abs sub" style="left:24px;top:249px">Earning</h4>
    <span class="abs earn-label" style="left:25px;top:288px">Low End</span>
    <span class="abs earn-value" style="left:25px;top:311px">$33, 000</span>
    <span class="abs earn-label" style="left:136px;top:288px">Median</span>
    <span class="abs earn-value" style="left:136px;top:311px">$33, 000</span>
    <span class="abs earn-label" style="left:239px;top:288px">High End</span>
    <span class="abs earn-value" style="left:239px;top:311px">$33, 000</span>
    <span class="pill btn-learn">Learn More</span>
    <div class="video" role="img" aria-label="Video still of a plumber tightening a sink drain pipe with a red wrench">
      <svg class="abs" style="left:200px;top:136px" width="46" height="50" viewBox="0 0 46 50"><path d="M4 2 L44 25 L4 48 Z" fill="#fff" stroke="#fff" stroke-width="4" stroke-linejoin="round"/></svg>
    </div>
  </article>

  <h2 class="abs section-title" style="top:709px">Classes</h2>
  <a class="abs view-all">View All</a>

  <article class="card class-card" style="left:70px">
    <div class="class-head" style="background:var(--ink)">
      <div class="who"><svg width="16" height="16" viewBox="0 0 16 16"><circle cx="8" cy="4.5" r="4" fill="#fff"/><path d="M0 16c0-5 3.5-6.5 8-6.5s8 1.5 8 6.5z" fill="#fff"/></svg>Math Teacher</div>
      <div class="period">Period 1</div>
      <div class="course">8th Grade Math/Pre-Algebra</div>
    </div>
    <div class="class-brand">Trailpoint Careers<small>8TH GRADE MATH</small></div>
    <span class="pill btn-class">Go to Class</span>
  </article>

  <article class="card class-card" style="left:387px">
    <div class="class-head" style="background:var(--teal)">
      <div class="who"><svg width="16" height="16" viewBox="0 0 16 16"><circle cx="8" cy="4.5" r="4" fill="#fff"/><path d="M0 16c0-5 3.5-6.5 8-6.5s8 1.5 8 6.5z" fill="#fff"/></svg>Math Teacher</div>
      <div class="period">Period 6</div>
      <div class="course">Algebra 1</div>
    </div>
    <div class="class-brand">Trailpoint Careers<small>ALGEBRA</small></div>
    <span class="pill btn-class">Go to Class</span>
  </article>

  <article class="card class-card" style="left:722px">
    <div class="class-head" style="background:var(--rust)">
      <div class="who"><svg width="16" height="16" viewBox="0 0 16 16"><circle cx="8" cy="4.5" r="4" fill="#fff"/><path d="M0 16c0-5 3.5-6.5 8-6.5s8 1.5 8 6.5z" fill="#fff"/></svg>Math Teacher</div>
      <div class="period">Period 5</div>
      <div class="course">Algebra 1</div>
    </div>
    <div class="class-brand">Trailpoint Careers<small>ALGEBRA</small></div>
    <span class="pill btn-class">Go to Class</span>
  </article>

  <div class="rule" style="left:70px;top:1087px;width:976px;background:#6A6A6A"></div>

  <h2 class="abs section-title" style="top:1117px">Upcoming Lessons</h2>
  <article class="card" style="left:70px;top:1177px;width:976px;height:302px">
    <p class="abs lessons-lead">Lessons&nbsp; due up to the next 7 days:</p>
    <div class="rule" style="left:24px;top:67px;width:928px"></div>
    <span class="abs col-head" style="left:24px;top:85px">Class</span>
    <span class="abs col-head" style="left:223px;top:85px">Lesson</span>
    <span class="abs col-head" style="left:655px;top:85px">Due</span>
    <div class="rule" style="left:24px;top:119px;width:928px"></div>

    <span class="abs cell" style="left:24px;top:130px">Period 1</span>
    <span class="abs cell" style="left:223px;top:130px">1.1 Translation</span>
    <span class="abs cell" style="left:655px;top:130px">October 15th at 11:59pm</span>
    <div class="rule" style="left:24px;top:163px;width:928px"></div>

    <span class="abs cell" style="left:24px;top:170px">Period 1</span>
    <span class="abs cell" style="left:223px;top:170px">2.1 Operations with Rational Numbers</span>
    <span class="abs cell" style="left:655px;top:170px">October 15th at 11:59pm</span>
    <div class="rule" style="left:24px;top:203px;width:928px"></div>

    <span class="abs cell" style="left:24px;top:210px">Period 1</span>
    <span class="abs cell" style="left:223px;top:210px">3.1 Operations with Rational Numbers</span>
    <span class="abs cell" style="left:655px;top:210px">October 15th at 11:59pm</span>
    <div class="rule" style="left:24px;top:244px;width:928px"></div>

    <span class="abs cell" style="left:24px;top:251px">Period 1</span>
    <span class="abs cell" style="left:223px;top:251px">4.1 Operations with Rational Numbers</span>
    <span class="abs cell" style="left:655px;top:251px">October 15th at 11:59pm</span>
  </article>
</section>

</body>
</html>
```